Parkinson's Disease Progression

Visually describe the rate of Parkinson progression in the first 15 years following diagnosis. Title: "Patient-Perceived Progression of Parkinsonism"

The attached figure names "meanqol" is the curve that should serve as the basis of this graphic. Everything else-- color, labels, font, etc. describe this curve.
Thank you!

Target Market(s)

People with Parkisnon's Disease, neurologists, family members.

Font styles to use
Sans Serif

Requirements
Must have
• Must have the lines going through these exact numbers
Excellent -- 502
Very good- 661
Good- 895
Fair- 1268
Poor- 1655

LABELS:
Title: "Patient-Perceived Progression of Parkinsonism"
"SWI-TC (Self-Logged Wellbeing Index for Tremor Conditions)" should be the label on the left.
"Quality of Life" should be the label on the right
"Years Since Diagnosis" should be the label on the bottom
Nice to have
• A color scheme that goes from GOOD (low numbers) to BAD (high numbers).

Easy to read (elderly)

```html
<!DOCTYPE html>
<html lang="en">
<head>
<meta charset="utf-8">
<title>SWI-TC Quality of Life by Years Since Diagnosis</title>
<link rel="stylesheet" href="https://fonts.googleapis.com/css2?family=Arimo:wght@700&display=swap">
<style>
  :root {
    --ink: #111111;
    --paper: #ffffff;
    --band-poor: #ee4868;
    --band-fair: #f59997;
    --band-good: #f9cdab;
    --band-very-good: #c6c6a9;
    --band-excellent: #86ae9b;
    --trend: #00aeef;
    --range-edge: #3b3f5c;
  }
  html, body {
    margin: 0;
    padding: 0;
    width: 1200px;
    height: 708px;
    overflow: hidden;
    background: var(--paper);
  }
  .chart {
    display: block;
    width: 1200px;
    height: 708px;
    font-family: "Arimo", Arial, Helvetica, sans-serif;
    font-weight: 700;
    fill: var(--ink);
  }
  .band-poor { fill: var(--band-poor); }
  .band-fair { fill: var(--band-fair); }
  .band-good { fill: var(--band-good); }
  .band-very-good { fill: var(--band-very-good); }
  .band-excellent { fill: var(--band-excellent); }
  .range-fill { fill: var(--paper); }
  .range-edge { fill: none; stroke: var(--range-edge); stroke-width: 1.4; stroke-dasharray: 4 3; }
  .trend-line { fill: none; stroke: var(--trend); stroke-width: 7; stroke-linecap: round; }
  .axis-line { stroke: var(--ink); stroke-width: 4; fill: none; }
  .tick-major { stroke: var(--ink); stroke-width: 4; }
  .tick-minor { stroke: var(--ink); stroke-width: 2.5; }
  .tick-label { font-size: 31px; }
  .y-label { text-anchor: end; dominant-baseline: middle; }
  .x-label { text-anchor: middle; }
  .axis-title { font-size: 50px; }
  .axis-subtitle { font-size: 21px; }
  .category-label { font-size: 23px; dominant-baseline: middle; }
</style>
</head>
<body>
<svg class="chart" viewBox="0 0 1548 913" role="img" aria-label="SWI-TC score over 15 years since diagnosis, with quality of life bands">
  <!-- Quality of life bands -->
  <g class="bands">
    <rect class="band-poor" x="330" y="142.5" width="878" height="144.2"/>
    <rect class="band-fair" x="330" y="286.7" width="878" height="138.9"/>
    <rect class="band-good" x="330" y="425.6" width="878" height="87.2"/>
    <rect class="band-very-good" x="330" y="512.8" width="878" height="59.2"/>
    <rect class="band-excellent" x="330" y="572" width="878" height="187"/>
  </g>

  <!-- Confidence range and mean trend -->
  <g class="trend">
    <path class="range-fill" d="M330,557 C400,540 500,500 580,482 C620,474 700,472 740,472 C800,470 840,445 930,410 C1000,385 1040,370 1080,355 C1140,335 1190,310 1208,298 L1208,410 C1190,400 1160,398 1120,398 C1080,398 1040,400 960,420 C880,445 820,480 760,495 C720,502 680,497 620,502 C580,505 540,520 480,545 C420,570 370,600 330,634 Z"/>
    <path class="range-edge" d="M330,557 C400,540 500,500 580,482 C620,474 700,472 740,472 C800,470 840,445 930,410 C1000,385 1040,370 1080,355 C1140,335 1190,310 1208,298"/>
    <path class="range-edge" d="M330,634 C370,600 420,570 480,545 C540,520 580,505 620,502 C680,497 720,502 760,495 C820,480 880,445 960,420 C1040,400 1080,398 1120,398 C1160,398 1190,400 1208,410"/>
    <path class="trend-line" d="M330,597 C420,560 520,505 580,493 C620,486 660,488 700,487 C760,486 790,478 830,460 C880,437 940,410 990,395 C1050,373 1120,365 1208,354"/>
  </g>

  <!-- Axes -->
  <g class="axes">
    <line class="axis-line" x1="330" y1="89" x2="330" y2="759"/>
    <line class="axis-line" x1="1208" y1="89" x2="1208" y2="759"/>
    <line class="axis-line" x1="310" y1="759" x2="1210" y2="759"/>

    <g class="y-ticks">
      <line class="tick-major" x1="308" y1="89" x2="340" y2="89"/>
      <line class="tick-major" x1="308" y1="163.5" x2="340" y2="163.5"/>
      <line class="tick-major" x1="308" y1="238" x2="340" y2="238"/>
      <line class="tick-major" x1="308" y1="312.5" x2="340" y2="312.5"/>
      <line class="tick-major" x1="308" y1="387" x2="340" y2="387"/>
      <line class="tick-major" x1="308" y1="461.5" x2="340" y2="461.5"/>
      <line class="tick-major" x1="308" y1="536" x2="340" y2="536"/>
      <line class="tick-major" x1="308" y1="610.5" x2="340" y2="610.5"/>
      <line class="tick-major" x1="308" y1="685" x2="340" y2="685"/>
      <line class="tick-minor" x1="322" y1="126.3" x2="338" y2="126.3"/>
      <line class="tick-minor" x1="322" y1="200.8" x2="338" y2="200.8"/>
      <line class="tick-minor" x1="322" y1="275.3" x2="338" y2="275.3"/>
      <line class="tick-minor" x1="322" y1="349.8" x2="338" y2="349.8"/>
      <line class="tick-minor" x1="322" y1="424.3" x2="338" y2="424.3"/>
      <line class="tick-minor" x1="322" y1="498.8" x2="338" y2="498.8"/>
      <line class="tick-minor" x1="322" y1="573.3" x2="338" y2="573.3"/>
      <line class="tick-minor" x1="322" y1="647.8" x2="338" y2="647.8"/>
      <line class="tick-minor" x1="322" y1="722.3" x2="338" y2="722.3"/>
    </g>

    <g class="tick-label y-label">
      <text x="296" y="91">1800</text>
      <text x="296" y="165.5">1600</text>
      <text x="296" y="240">1400</text>
      <text x="296" y="314.5">1200</text>
      <text x="296" y="389">1000</text>
      <text x="296" y="463.5">800</text>
      <text x="296" y="538">600</text>
      <text x="296" y="612.5">400</text>
      <text x="296" y="687">200</text>
    </g>

    <g class="x-ticks">
      <line class="tick-major" x1="330" y1="738" x2="330" y2="780"/>
      <line class="tick-major" x1="622.7" y1="738" x2="622.7" y2="780"/>
      <line class="tick-major" x1="915.3" y1="738" x2="915.3" y2="780"/>
      <line class="tick-major" x1="1208" y1="738" x2="1208" y2="780"/>
      <line class="tick-minor" x1="388.5" y1="748" x2="388.5" y2="772"/>
      <line class="tick-minor" x1="447.1" y1="748" x2="447.1" y2="772"/>
      <line class="tick-minor" x1="505.6" y1="748" x2="505.6" y2="772"/>
      <line class="tick-minor" x1="564.1" y1="748" x2="564.1" y2="772"/>
      <line class="tick-minor" x1="681.2" y1="748" x2="681.2" y2="772"/>
      <line class="tick-minor" x1="739.7" y1="748" x2="739.7" y2="772"/>
      <line class="tick-minor" x1="798.3" y1="748" x2="798.3" y2="772"/>
      <line class="tick-minor" x1="856.8" y1="748" x2="856.8" y2="772"/>
      <line class="tick-minor" x1="973.9" y1="748" x2="973.9" y2="772"/>
      <line class="tick-minor" x1="1032.4" y1="748" x2="1032.4" y2="772"/>
      <line class="tick-minor" x1="1090.9" y1="748" x2="1090.9" y2="772"/>
      <line class="tick-minor" x1="1149.5" y1="748" x2="1149.5" y2="772"/>
    </g>

    <g class="tick-label x-label">
      <text x="283" y="816">0</text>
      <text x="622.7" y="816">5</text>
      <text x="915.3" y="816">10</text>
      <text x="1208" y="816">15</text>
    </g>
  </g>

  <!-- Band names -->
  <g class="category-label">
    <text x="1235" y="211">Poor</text>
    <text x="1235" y="347">Fair</text>
    <text x="1235" y="467">Good</text>
    <text x="1235" y="541">Very Good</text>
    <text x="1235" y="653">Excellent</text>
  </g>

  <!-- Axis titles -->
  <text class="axis-title" x="755" y="893" text-anchor="middle">Years Since Diagnosis</text>
  <g transform="translate(120 415) rotate(-90)">
    <text class="axis-title" x="0" y="0" text-anchor="middle" dominant-baseline="middle">SWI-TC</text>
  </g>
  <g transform="translate(160 415) rotate(-90)">
    <text class="axis-subtitle" x="0" y="0" text-anchor="middle" dominant-baseline="middle">(Self-Logged Wellbeing Index for Tremor Conditions)</text>
  </g>
  <g transform="translate(1448 400) rotate(-90)">
    <text class="axis-title" x="0" y="0" text-anchor="middle" dominant-baseline="middle">Quality of Life</text>
  </g>
</svg>
</body>
</html>
```